Fresh pet feed direct from manufacturer to door step. Quality and Freshness un-surpassed in Industr

Need Business Card Design; leading into many other projects, for New Franchised Business Opportunity providing home delivery of fresh dog and cat feed (no emphasis needed for cat) direct from manufacturing facility. (no middle men or distributors) Food is Farm to Factory fresh. Our trademarked tagline is "Quality is our MAIN Ingredient ! "
Updates

Please take note of other contest for Chirplane Cover and Profile Pic's

Target Market(s)

Dog and Cat owners

Industry/Entity Type

Pet

Contact Information for Business Card

Name, address, local phone, national 800 number, website, email address

Other font styles liked:
• follow that from logo

Requirements
Must have
• Our feed is made in Texas with ingredients sourced from local farms. We want to lean heavy on the Made in West Texas , ranch theme but that has a 'black label', 'vantrel', 'premium', 'high-end' look and feel
Nice to have
• maybe have an offer on card? 20% off with promo code "x" etc.. ?? just a thought...

```html
<!DOCTYPE html>
<html lang="en">
<head>
<meta charset="utf-8">
<title>Ranchmark Business Card</title>
<link rel="stylesheet" href="https://fonts.googleapis.com/css2?family=Cinzel:wght@400;600&display=swap">
<style>
  :root {
    --backdrop: #1e1f1f;
    --card-white: #ffffff;
    --ink: #1a1a1a;
    --card-black: #1c1e1d;
    --pattern-dark: #262827;
    --pattern-mid: #4a4c4b;
    --pattern-light: #8e8f8e;
    --card-edge: #3a3c3b;
  }
  * { margin: 0; padding: 0; box-sizing: border-box; }
  html, body { width: 1200px; height: 675px; overflow: hidden; }
  body {
    background: var(--backdrop);
    display: flex;
    align-items: center;
    justify-content: center;
    gap: 60px;
    font-family: "Cinzel", serif;
  }
  .card {
    width: 500px;
    height: 286px;
    border-radius: 2px;
    position: relative;
    box-shadow: 0 10px 28px rgba(0, 0, 0, 0.55);
  }
  .card-front {
    background: var(--card-white);
    color: var(--ink);
  }
  .brand {
    position: absolute;
    top: 44px;
    left: 0;
    right: 0;
    display: flex;
    align-items: center;
    justify-content: center;
    gap: 12px;
  }
  .brand-dot {
    width: 16px;
    height: 16px;
    border-radius: 50%;
    background: var(--ink);
  }
  .brand-name {
    font-size: 30px;
    font-weight: 600;
    letter-spacing: 2px;
    color: var(--ink);
  }
  .contact {
    position: absolute;
    left: 150px;
    top: 120px;
    line-height: 1.35;
  }
  .contact-name {
    font-size: 20px;
    font-weight: 600;
    letter-spacing: 1px;
    margin-bottom: 8px;
  }
  .contact-line {
    font-size: 12px;
    letter-spacing: 0.5px;
  }
  .contact-gap { height: 8px; }
  .card-back {
    background: var(--card-black);
    border: 1px solid var(--card-edge);
    overflow: hidden;
  }
  .paw-pattern {
    position: absolute;
    inset: 0;
    background:
      radial-gradient(ellipse 60% 70% at 30% 35%, rgba(142, 143, 142, 0.35), transparent 70%),
      radial-gradient(ellipse 55% 65% at 75% 70%, rgba(142, 143, 142, 0.28), transparent 70%),
      linear-gradient(135deg, var(--pattern-mid) 0%, var(--pattern-dark) 55%, var(--card-black) 100%);
  }
</style>
</head>
<body>
  <section class="card card-front">
    <div class="brand">
      <span class="brand-dot"></span>
      <span class="brand-name">RANCHMARK</span>
    </div>
    <div class="contact">
      <p class="contact-name">Dale Hendry</p>
      <p class="contact-line">1870 Mesa Ridge Rd</p>
      <p class="contact-line">Lubbock, TX 79401</p>
      <div class="contact-gap"></div>
      <p class="contact-line">806 555 0142</p>
      <p class="contact-line">800 555 0199</p>
      <p class="contact-line">www.ranchmarkfeed.com</p>
    </div>
  </section>
  <section class="card card-back">
    <div class="paw-pattern" role="img" aria-label="Repeating pattern of light grey paw prints scattered across the black card back"></div>
  </section>
</body>
</html>
```